Elegant Business Card for Technology Company

Client is a supplier of innovative industrial communications and automation equipment since 2002. This contest is to gather fresh ideas for a redesign of the existing business card. Client is looking for design that best communicates tagline "Industrial Networking and Computing Specialist".

Design submissions should look modern, clean, elegant and professional. It should not be cluttered. Use white as the primary colour. Orange and black as secondary colour. Refer to jpeg File 1 on the current design.

Fonts used by Client used include Arial Regular, Arial Black, Roboto Regular, Roboto Black and Lato.

The winning design will be sent for offset printing using super white 250gsm artcard paper (open for suggestions).

Target Market(s)

System Engineers, Project Managers, Purchasing Managers from companies providing engineering services for Smart Cities.

Industry/Entity Type

Information Technology

Contact Information for Business Card

Refer to PDF File 3 for Business Card Details. Priority of short contact information would be as follows Name > Job Title > Email > Mobile > Web > Tel > Fax > Business Address >UEN (UEN represents company registration number)

Font styles to use
Sans Serif

Colors
ffffff
f37122
000000
5c5c5c

Requirements
Must have
• Refer to AI File 2 (Company Logo) & PDF File 3 (Information on Namecard)
Should not have
• No QR codes
• No Social Media Icons
• Do not create full Black or Orange colour background

```html
<!DOCTYPE html>
<html lang="en">
<head>
<meta charset="utf-8">
<title>KVR Business Card</title>
<link rel="stylesheet" href="https://fonts.googleapis.com/css2?family=Roboto:ital,wght@0,400;0,700;0,900;1,400&display=swap">
<style>
  :root {
    --white: #ffffff;
    --orange: #f37122;
    --black: #000000;
    --grey: #5c5c5c;
    --backdrop: #e9e9e9;
  }
  * { margin: 0; padding: 0; box-sizing: border-box; }
  html, body { width: 1200px; height: 900px; overflow: hidden; }
  body {
    background: var(--backdrop);
    font-family: "Roboto", Arial, sans-serif;
    position: relative;
  }
  .card {
    position: absolute;
    left: 230px;
    width: 740px;
    height: 423px;
    background: var(--white);
    overflow: hidden;
    box-shadow: 0 4px 14px rgba(0,0,0,0.18);
  }
  .card--front { top: 18px; }
  .card--back { top: 459px; }
  .card-art { position: absolute; inset: 0; }

  /* Front */
  .brand {
    position: absolute;
    left: 60px; top: 62px;
    display: flex; align-items: center; gap: 16px;
  }
  .brand-dot { width: 34px; height: 34px; border-radius: 50%; background: var(--orange); }
  .brand-name { font-weight: 900; font-size: 86px; color: var(--black); letter-spacing: 2px; line-height: 1; }
  .address {
    position: absolute;
    left: 62px; top: 266px;
    color: var(--orange);
    font-style: italic;
    font-size: 19px;
    line-height: 1.3;
  }
  .person { position: absolute; left: 438px; top: 36px; width: 260px; }
  .person-name { font-weight: 900; font-size: 29px; color: var(--black); }
  .person-title {
    font-weight: 700; font-size: 18px; color: var(--white);
    padding-bottom: 5px; border-bottom: 2px solid var(--white);
    margin-bottom: 14px;
  }
  .contact-list { list-style: none; font-size: 17.5px; color: var(--black); line-height: 1.3; }
  .contact-list strong { font-weight: 700; }
  .reg-number { margin-top: 28px; font-size: 17px; color: var(--black); }
  .reg-number span { font-size: 22px; }

  /* Back */
  .services { list-style: none; position: absolute; inset: 0; }
  .service {
    position: absolute;
    font-weight: 900;
    font-size: 21px;
    text-transform: uppercase;
    line-height: 36px;
    height: 36px;
    white-space: nowrap;
  }
  .service--on-band { color: var(--white); }
  .service--on-white { color: var(--orange); }
</style>
</head>
<body>

<section class="card card--front" aria-label="Business card front">
  <svg class="card-art" width="740" height="423" viewBox="0 0 740 423" aria-hidden="true">
    <path d="M335 0 C392 110 380 290 300 423" fill="none" stroke="var(--orange)" stroke-width="5"/>
    <path d="M358 0 C420 120 400 300 322 423 L740 423 L740 0 Z" fill="var(--orange)"/>
    <path d="M372 0 C430 120 412 300 338 423" fill="none" stroke="var(--white)" stroke-width="4"/>
  </svg>

  <div class="brand">
    <span class="brand-dot"></span>
    <span class="brand-name">KVR</span>
  </div>

  <address class="address">
    22 Harbour Link<br>
    Business Park #05-12 (Lobby B)<br>
    Singapore 409120
  </address>

  <div class="person">
    <h1 class="person-name">Daniel Koh</h1>
    <p class="person-title">Sales Manager</p>
    <ul class="contact-list">
      <li>E-mail: sales@kvr-systems.sg</li>
      <li>Mobile: +65 9000 1234</li>
      <li>Web: <strong>www.kvr-systems.sg</strong></li>
      <li>Tel: +65 6100 2200</li>
      <li>Fax: +65 6100 2201</li>
    </ul>
    <p class="reg-number">UEN No: <span>201504117K</span></p>
  </div>
</section>

<section class="card card--back" aria-label="Business card back">
  <svg class="card-art" width="740" height="423" viewBox="0 0 740 423" aria-hidden="true">
    <rect x="0" y="72" width="740" height="36" fill="var(--orange)"/>
    <rect x="0" y="152" width="740" height="36" fill="var(--orange)"/>
    <rect x="0" y="232" width="740" height="36" fill="var(--orange)"/>
    <rect x="0" y="312" width="740" height="36" fill="var(--orange)"/>
    <circle cx="-120" cy="211" r="320" fill="var(--white)" stroke="var(--orange)" stroke-width="5"/>
  </svg>

  <ul class="services">
    <li class="service service--on-band"  style="left:198px; top:72px;">Industrial Networking</li>
    <li class="service service--on-white" style="left:212px; top:112px;">and Computing Specialist</li>
    <li class="service service--on-band"  style="left:219px; top:152px;">Industrial Ethernet / Wireless / Cellular</li>
    <li class="service service--on-white" style="left:222px; top:192px;">Industrial and Embedded Computing</li>
    <li class="service service--on-band"  style="left:220px; top:232px;">Serial / Fieldbus Connectivity</li>
    <li class="service service--on-white" style="left:212px; top:272px;">IP Video Surveillance</li>
    <li class="service service--on-band"  style="left:199px; top:312px;">Remote Automation</li>
  </ul>
</section>

</body>
</html>
```